Corvane Lift Inc Website Deisgn

We are a new small elevator contracting company.
We would like a full website designed similar to
http://pellusk-lifts.example or https://www.marbolt-hoistworks.example/
In addition to contents found on the above webpages.. we would like a section for project gallery etc.... have fun with it ... make it professional

Target Market(s)

Elevator Consultants - Property managers - Condo Boards - Commercial office buildings

Coding

Coded - Design and coding required

Number of Pages Required

5+ page

Requirements
Must have
• Navigation Bar.. Be view able via mobile ..Should be pictures of Tall Office buildings in background.. Toronto city skyline etc....

Have Fun!

```html
<!DOCTYPE html>
<html lang="en">
<head>
<meta charset="utf-8">
<title>Corvane Lift Inc — FAQ</title>
<link rel="stylesheet" href="https://fonts.googleapis.com/css2?family=Open+Sans:wght@400;600;700&display=swap">
<style>
:root{
  --navy:#302e66;
  --ink:#333333;
  --muted:#7a7a7a;
  --bar:#cccccc;
  --rule:#2d4a6b;
  --white:#ffffff;
  --steel:#2f5878;
  --brand-ink:#2a2426;
}
*{box-sizing:border-box;margin:0;padding:0}
html,body{width:1200px;height:3777px;overflow:hidden;background:var(--white)}
body{position:relative;font-family:"Open Sans",Arial,sans-serif;color:var(--ink)}
.hero{position:absolute;left:0;top:0;width:1200px;height:2131px;overflow:hidden}
.hero-photo{position:absolute;inset:0;background:linear-gradient(180deg,#c3c4cc 0%,#b6b8c2 35%,#9a9ca8 60%,#8a8c98 100%)}
.brand-name{position:absolute;left:197px;top:905px;font-size:80px;font-weight:700;color:var(--brand-ink);white-space:nowrap;line-height:1}
.hero-cta{position:absolute;left:267px;top:1198px;width:400px;height:160px;border-radius:80px;background:var(--steel)}
.nav-panel{position:absolute;left:392px;top:0;width:808px;height:2131px;background:var(--navy)}
.nav-close{position:absolute;left:1096px;top:98px}
.nav-list{list-style:none;position:absolute;left:478px;top:0}
.nav-list li{position:absolute;left:0;white-space:nowrap;font-size:52px;font-weight:600;color:var(--white);line-height:1}
.faq-title{position:absolute;left:0;width:1200px;top:2240px;display:flex;justify-content:center;align-items:center;gap:22px;font-size:70px;font-weight:600;color:var(--ink);line-height:1}
.faq-item{position:absolute;left:43px;width:1114px}
.faq-q{height:116px;background:var(--bar);display:flex;align-items:center;justify-content:space-between;padding:0 44px;font-size:38px;font-weight:600;color:#2b2b2b;white-space:nowrap}
.faq-a{background:var(--white);box-shadow:0 6px 18px rgba(0,0,0,.18);padding:36px 70px 36px 44px;font-size:31px;line-height:52px;color:#222;height:344px;overflow:hidden}
.learn-more{position:absolute;left:0;width:1200px;top:3470px;text-align:center;font-size:50px;font-weight:700;color:var(--navy)}
.footer-rule{position:absolute;left:0;top:3654px;width:1200px;height:5px;background:var(--rule)}
.to-top{position:absolute;left:1069px;top:3612px;width:88px;height:88px;border-radius:50%;background:#000;display:flex;align-items:center;justify-content:center}
.copyright{position:absolute;left:0;width:1200px;top:3698px;text-align:center;font-size:34px;color:var(--muted)}
</style>
</head>
<body>
<header class="hero">
  <div class="hero-photo" role="img" aria-label="Toronto skyline of tall office towers, greyed tint"></div>
  <div class="brand-name">Corvane Lift Inc</div>
  <div class="hero-cta"></div>
  <nav class="nav-panel" aria-label="Main menu"></nav>
  <svg class="nav-close" width="64" height="64" viewBox="0 0 64 64" aria-label="Close menu"><path d="M8 8L56 56M56 8L8 56" stroke="#fff" stroke-width="12" stroke-linecap="round"/></svg>
  <ul class="nav-list">
    <li style="top:320px">SERVICES</li>
    <li style="top:471px">PROJECTS</li>
    <li style="top:622px">ABOUT US</li>
    <li style="top:772px">CONTACT US</li>
    <li style="top:923px">FAQ</li>
    <li style="top:1062px">PRIVACY POLICY</li>
    <li style="top:1199px">TERMS AND CONDITION</li>
  </ul>
</header>

<main>
  <h2 class="faq-title">
    <svg width="58" height="58" viewBox="0 0 58 58" aria-hidden="true"><circle cx="29" cy="29" r="29" fill="var(--navy)"/><circle cx="29" cy="16" r="5" fill="#fff"/><rect x="24" y="25" width="10" height="22" rx="2" fill="#fff"/></svg>
    FAQ
  </h2>

  <div class="faq-item" style="top:2395px">
    <div class="faq-q"><span>Lorem ipsum dolor sit amet, consectetur adipiscing</span><svg width="18" height="12" viewBox="0 0 18 12"><path d="M3 9L9 3L15 9" stroke="#333" stroke-width="3" fill="none"/></svg></div>
    <div class="faq-a">Lorem ipsum dolor sit amet, consectetur adipiscing elit, sed do eiusmod tempor incididunt ut labore et dolore magna aliqua. Sed augue lacus viverra vitae congue. Est pellentesque elit ullamcorper dignissim cras. Libero enim sed faucibus turpis. Habitant morbi tristique senectus et netus et malesuada. Donec ...</div>
  </div>
  <div class="faq-item" style="top:2914px">
    <div class="faq-q"><span>Lorem ipsum dolor sit amet, consectetur adipiscing</span><svg width="18" height="12" viewBox="0 0 18 12"><path d="M3 3L9 9L15 3" stroke="#333" stroke-width="3" fill="none"/></svg></div>
  </div>
  <div class="faq-item" style="top:3088px">
    <div class="faq-q"><span>Lorem ipsum dolor sit amet, consectetur adipiscing</span><svg width="18" height="12" viewBox="0 0 18 12"><path d="M3 3L9 9L15 3" stroke="#333" stroke-width="3" fill="none"/></svg></div>
  </div>
  <div class="faq-item" style="top:3262px">
    <div class="faq-q"><span>Lorem ipsum dolor sit amet, consectetur adipiscing</span><svg width="18" height="12" viewBox="0 0 18 12"><path d="M3 3L9 9L15 3" stroke="#333" stroke-width="3" fill="none"/></svg></div>
  </div>

  <div class="learn-more">LEARN MORE <svg width="50" height="30" viewBox="0 0 50 30" style="vertical-align:middle"><path d="M2 15H40M30 4L45 15L30 26" stroke="var(--navy)" stroke-width="6" fill="none"/></svg></div>
</main>

<footer>
  <div class="footer-rule"></div>
  <div class="to-top"><svg width="30" height="36" viewBox="0 0 30 36"><path d="M15 34V4M5 14L15 3L25 14" stroke="#fff" stroke-width="4" fill="none"/></svg></div>
  <p class="copyright">Copyright © CorvaneLift. All rights reserved.</p>
</footer>
</body>
</html>
```